Cover design brief for the “Lanterns along the river” collection

This collection aims to publish articles by several authors who are practitioners specializing in sociocracy, a participatory mode of governance that is highly innovative, and even quite subversive of the autocratic way in which companies and public institutions operate. However, this method has been widely and increasingly implemented since its initial development in the Netherlands in the 1970s and 80s. It is currently of particular interest to non-profit and cooperative organizations, citizen projects and intentional communities, as well as IT work teams (due to its proximity to the spirit of Agile methods).
The content is intellectually demanding. It won't be a matter of popularization for promotional purposes, but rather of subjects for reflection or in-depth analysis of practices, and feedback from field experience. Nor is it an academic journal.
The language used for these publications is French.
The target audience is French-speaking Europe and Canada.

Target Market(s)

The collection is aimed both at other practitioners of this method who want to develop their knowledge, and at people interested in the subjects of collective intelligence, cooperation and organization, in response to social, ecological and/or political concerns.

Industry/Entity Type

Training and consultancy

Font styles to use
Sans Serif

Requirements
Must have
• The name of the collection: Lanterns along the river - Weaving a quieter commons Each volume will mention the name of the collection as well as the theme of the volume. First one: Volume 1 - Mapping hidden currents within shared endeavours. Selection criteria: - A singular, recurring visual identity for the volumes in the collection, highlighting its theme. - Appeal to potential readers; arouse curiosity. - Good readability of the text (title and subtitle, authors; presentation on back cover). - Simplicity of design variation for the cover of subsequent volumes (changing only the text). - Reasonable price in relation to a hoped-for circulation of between 100 and 300 copies per volume (the theme is linked to a niche that is still fairly narrow in the French-speaking world).
Nice to have
• Suggested graphic design directions If you have another direction to suggest with convincing arguments, we're open to your proposal. - The name of the collection, and in particular "Lanterns along the river", will be visible at first glance. - The overall visual impression is one of movement and dynamism. - The style will be based on illustration work, such as sketchnotes. - The tone is playful and humorous. For example, it may mirror back to the potential reader the cultural clichés and social norms about power that make the theme "lanterns along the river" a challenge to his or her imagination. As stated in the preface to Volume 1: "Most people are used to social environments where the choice is limited to suffering or fighting against powers that seek in a multitude of ways to put us at their service..."

```html
<!DOCTYPE html>
<html lang="en">
<head>
<meta charset="utf-8">
<title>Lanterns along the river – Volume 1</title>
<link rel="stylesheet" href="https://fonts.googleapis.com/css2?family=Oswald:wght@500;700&family=Montserrat:wght@300;400;700;800&display=swap">
<style>
  :root {
    --backdrop: #323031;
    --paper: #ffffff;
    --ink: #111111;
    --red-deep: #9c1d2a;
    --red-bright: #dc2a42;
    --note: #d4ea0e;
    --mark-soft: #f1b3bd;
    --mark-strong: #e0566b;
  }
  * { margin: 0; padding: 0; box-sizing: border-box; }
  html, body { width: 1200px; height: 675px; overflow: hidden; background: var(--backdrop); }
  .cover {
    position: absolute; left: 393px; top: 0; width: 469px; height: 675px;
    background: var(--paper); overflow: hidden; color: var(--ink);
  }
  .volume-theme {
    position: absolute; top: 10px; left: 0; right: 0; text-align: center;
    font-family: "Montserrat", sans-serif; font-weight: 400; font-size: 15.5px;
    letter-spacing: 0.16em; line-height: 22px; text-transform: uppercase;
  }
  .volume-theme .volume-number { font-weight: 800; }
  .title-big {
    position: absolute; left: 0; right: 0; text-align: center;
    font-family: "Oswald", sans-serif; font-weight: 700; line-height: 1;
    text-transform: uppercase;
    background: linear-gradient(90deg, var(--red-deep) 0%, var(--red-bright) 45%, var(--red-bright) 60%, var(--red-deep) 100%);
    -webkit-background-clip: text; background-clip: text; color: transparent;
  }
  .title-lanterns { top: 109px; font-size: 100px; letter-spacing: -1px; transform: scaleY(1.35); transform-origin: top center; }
  .title-river { top: 282px; font-size: 128px; letter-spacing: -1px; transform: scaleY(1.08); transform-origin: top center; }
  .title-ruled {
    position: absolute; top: 244px; left: 0; right: 0;
    display: flex; align-items: center; justify-content: center; gap: 12px;
    font-family: "Oswald", sans-serif; font-weight: 700; font-size: 44px; line-height: 1;
    text-transform: uppercase;
  }
  .title-ruled .rule { width: 90px; height: 5px; background: var(--ink); clip-path: polygon(0 50%, 100% 0, 100% 100%); }
  .title-ruled .rule.right { clip-path: polygon(0 0, 100% 50%, 0 100%); }
  .pinned-note {
    position: absolute; left: 96px; top: 389px; width: 140px; height: 140px;
    background: var(--note); transform: rotate(8deg);
  }
  .crossed-word {
    position: absolute; left: 252px; top: 420px; width: 108px; height: 104px;
    background: linear-gradient(135deg, var(--mark-soft), var(--mark-strong));
  }
  .collection-subtitle {
    position: absolute; top: 556px; left: 0; right: 0; text-align: center;
    font-family: "Montserrat", sans-serif; font-weight: 300; font-size: 16px;
    letter-spacing: 0.18em; line-height: 21px; text-transform: uppercase;
  }
  .authors {
    position: absolute; top: 612px; left: 0; right: 0; text-align: center;
    font-family: "Montserrat", sans-serif; font-weight: 800; font-size: 25px;
    letter-spacing: 0.1em; line-height: 27px; text-transform: uppercase;
  }
</style>
</head>
<body>
  <main class="cover">
    <p class="volume-theme"><span class="volume-number">“Volume 1”</span>- Mapping hidden currents<br>within shared endeavours</p>

    <h1>
      <span class="title-big title-lanterns">Lanterns</span>
      <span class="title-ruled"><span class="rule"></span>Along the<span class="rule right"></span></span>
      <span class="title-big title-river">River</span>
    </h1>

    <div class="pinned-note" role="img" aria-label="Lime sticky note pinned with a green push pin, reading SOCIOCRACY"></div>
    <div class="crossed-word" role="img" aria-label="The word AUTOCRACY struck out by a red brushed cross"></div>

    <p class="collection-subtitle">Weaving a<br>quieter commons</p>

    <p class="authors">Élise Marchand<br>Julien Caradec</p>
  </main>
</body>
</html>
```